Word Bureau Ostrelle Templates

We run a large number of businesses, including schools, airports, hotels and offices. We write reports on a daily basis and are looking for a strong and sexy WORD Template. We already have a logo in place (see graphical chart attached), that is rights' protected. We are looking for a beautiful wich reflect modern design and human aspects. Our logo has 2 design, full fill and watermark. It can be used in red or black.

Architects, Fire brigade, Building investors, contactors

• Arial, Calibri, ...

• Cover page, summary, Bullet points, Tables, Figures, Annex

```html
<!DOCTYPE html>
<html lang="en">
<head>
<meta charset="utf-8">
<title>Bureau Ostrelle – Report Template Pages</title>
<link href="https://fonts.googleapis.com/css2?family=Varela+Round&family=Hind:wght@400;500;600&family=Montserrat:wght@500&display=swap" rel="stylesheet">
<style>
:root{
  --red:#e4312b;
  --ink:#1d1d1d;
  --navy:#1f3b53;
  --canvas:#e3e3e3;
  --row:#e8e8e8;
  --white:#ffffff;
  --photo-warm:#8a6a3a;
  --photo-night:#1e2440;
}
*{margin:0;padding:0;box-sizing:border-box}
html,body{width:1200px;height:2442px;overflow:hidden;background:var(--canvas)}
body{position:relative;font-family:"Hind",Arial,sans-serif;color:var(--ink)}
.page{position:absolute;width:500px;height:706px;background:var(--white);overflow:hidden;box-shadow:0 14px 18px -10px rgba(0,0,0,.35)}
.page > *{position:absolute}
.page-label{position:absolute;width:500px;text-align:center;font-family:"Montserrat",sans-serif;font-weight:500;font-size:24px;color:var(--navy);letter-spacing:.5px}
.art{left:0;top:0}
/* footer */
.footer-rule{left:0;width:500px;top:662px;height:2px;background:var(--red)}
.footer-band{left:0;width:500px;top:667px;height:39px;background:var(--ink)}
.footer-url{left:22px;top:680px;font-family:"Varela Round",sans-serif;font-size:7.5px;letter-spacing:1.4px;color:var(--white)}
.footer-brand{left:220px;top:676px;display:flex;align-items:center;gap:5px}
.footer-brand .dot{width:11px;height:11px;border-radius:50%;background:var(--white)}
.footer-brand span{font-family:"Varela Round",sans-serif;font-size:8.5px;line-height:9px;color:var(--white)}
.footer-num{right:22px;top:680px;font-size:8px;color:var(--white)}
/* type */
.heading{left:22px;right:22px;display:flex;align-items:center;gap:10px;font-family:"Varela Round",sans-serif;color:var(--ink);white-space:nowrap}
.heading b{font-weight:400;color:var(--red)}
.heading::after{content:"";flex:1;height:1px;background:var(--red)}
.body-text{left:22px;width:456px;font-size:7.4px;line-height:11px;text-align:justify;color:#333}
.bar-heading{left:0;width:500px;height:24px;background:var(--ink);color:var(--red);font-family:"Varela Round",sans-serif;font-size:12px;text-align:center;line-height:25px}
.bullets{list-style:none;font-size:7.4px;color:#333}
.bullets li{position:relative;height:16.8px;padding-left:12px}
.bullets li::before{content:"";position:absolute;left:0;top:2.5px;width:4px;height:4px;border-radius:50%;background:var(--red)}
.bullets li.sub{margin-left:31px}
.bullets li.sub::before{width:6px;height:6px;border-radius:1px 1px 3px 3px;top:1.5px;left:-2px}
.bullets li.sub::after{content:"";position:absolute;left:-.5px;top:3px;width:2px;height:1px;border-left:1px solid #fff;border-bottom:1px solid #fff;transform:rotate(-45deg)}
/* cover */
.brand-light{left:60px;top:30px;display:flex;align-items:flex-start}
.brand-light span{font-family:"Varela Round",sans-serif;font-size:26px;line-height:28px;color:var(--white)}
.brand-dot{left:15px;top:43px;width:30px;height:30px;border-radius:50%;background:var(--white)}
.cover-title{left:23px;top:452px;font-family:"Varela Round",sans-serif;font-size:41px;line-height:52px;color:var(--ink)}
.cover-title b{font-weight:400;color:var(--red)}
.cover-rule{left:23px;top:621px;width:96px;height:5px;background:var(--red)}
.stars{left:23px;top:416px;display:flex;gap:13px}
/* page 4 */
.feature{width:150px;text-align:center;top:474px}
.feature h4{font-family:"Varela Round",sans-serif;font-weight:400;font-size:11px;color:var(--red);margin-top:12px}
.feature p{font-size:7.4px;line-height:11px;color:#333;margin-top:5px}
/* page 5 table */
.data-table{left:22px;top:175px;width:456px;border-collapse:separate;border-spacing:0;font-size:7.3px;color:#444}
.data-table th{height:18px;font-family:"Varela Round",sans-serif;font-weight:400;font-size:9px;color:var(--white);border-right:3px solid #fff}
.data-table th:last-child{border-right:0}
.data-table th.c1{background:var(--red)}
.data-table th.c2{background:#151515}
.data-table th.c3{background:#2c2c2c}
.data-table th.c4{background:#555}
.data-table th.c5{background:#878787}
.data-table td{height:22.6px;text-align:center}
.data-table td:first-child{text-align:left;padding-left:8px}
.data-table tr:nth-child(even) td{background:var(--row)}
.data-table thead tr:first-child{height:25px}
/* back */
.contact-text{left:0;width:500px;text-align:center;color:var(--white);font-family:"Varela Round",sans-serif}
.brand-dark{left:196px;top:428px;font-family:"Varela Round",sans-serif;font-size:34px;line-height:36px;color:var(--ink)}
.brand-dark-dot{left:137px;top:439px;width:36px;height:36px;border-radius:50%;background:var(--red)}
.contact-lines{left:0;width:500px;top:566px;text-align:center;font-size:13px;line-height:22px;color:var(--ink);font-weight:500}
</style>
</head>
<body>

<!-- PAGE 01 : cover -->
<section class="page" style="left:81px;top:59px">
  <svg class="art" width="500" height="706" viewBox="0 0 500 706">
    <path d="M0,0 H252 C190,62 100,132 0,212 Z" fill="var(--red)"/>
    <path d="M252,0 H318 C230,62 120,142 0,246 V212 C100,132 190,62 252,0 Z" fill="var(--ink)"/>
    <path d="M288,0 C198,125 152,292 236,440 C306,526 420,556 500,556 V0 Z" fill="var(--ink)"/>
    <path d="M316,0 C232,122 182,282 258,420 C320,500 420,530 500,530 V0 Z" fill="var(--photo-night)" role="img" aria-label="Photo of a lit palace facade behind palm trees at night"/>
    <circle cx="170" cy="197" r="92" fill="#fff"/>
    <circle cx="170" cy="197" r="87" fill="#9a9486" role="img" aria-label="Photo of a man working on a laptop by a window"/>
    <circle cx="274" cy="408" r="40" fill="#fff"/>
    <circle cx="274" cy="408" r="35" fill="var(--red)"/>
    <circle cx="425" cy="521" r="23" fill="#fff"/>
    <circle cx="425" cy="521" r="19" fill="var(--red)"/>
  </svg>
  <div class="brand-dot"></div>
  <div class="brand-light"><span>Bureau<br>Ostrelle</span></div>
  <svg class="stars" width="170" height="24" viewBox="0 0 170 24" aria-hidden="true">
    <g fill="none" stroke="var(--red)" stroke-width="2" stroke-linejoin="round">
      <path id="star" d="M12,2 L14.8,8.6 L21.8,9.2 L16.5,13.9 L18.1,20.8 L12,17.1 L5.9,20.8 L7.5,13.9 L2.2,9.2 L9.2,8.6 Z"/>
      <use href="#star" x="36"/><use href="#star" x="72"/><use href="#star" x="108"/><use href="#star" x="144"/>
    </g>
  </svg>
  <h1 class="cover-title" style="font-weight:400">Welcome to<br><b>Lorem Ipsum</b> Text<br>Goes Here</h1>
  <div class="cover-rule"></div>
  <div class="footer-rule"></div>
  <div class="footer-band"></div>
</section>
<div class="page-label" style="left:81px;top:783px">PAGE - 01</div>

<!-- PAGE 02 -->
<section class="page" style="left:624px;top:59px">
  <svg class="art" width="500" height="200" viewBox="0 0 500 200">
    <path d="M0,0 H500 V31 C400,110 300,148 210,148 C120,148 50,132 0,117 Z" fill="#5f6672" role="img" aria-label="Photo of people working at a desk with drawings and pens"/>
    <path d="M0,117 C50,132 120,148 210,148 C300,148 400,110 500,31 V74 C400,142 300,178 210,178 C120,178 50,168 0,164 Z" fill="var(--ink)"/>
    <circle cx="227" cy="161" r="28" fill="#fff"/><circle cx="227" cy="161" r="24" fill="var(--red)"/>
    <circle cx="425" cy="93" r="20" fill="#fff"/><circle cx="425" cy="93" r="16" fill="var(--red)"/>
  </svg>
  <h2 class="heading" style="top:218px;font-size:26px;font-weight:400"><span><b>Heading</b> One</span></h2>
  <p class="body-text" style="top:254px">Lorem Ipsum is simply dummy text of the printing and typesetting industry. Lorem Ipsum has been the industry's standard dummy text ever since the 1500s, when an unknown printer took a galley of type and scrambled it to make a type specimen book. It has survived not only five centuries, but also the leap into electronic typesetting, remaining essentially unchanged. It was popularised in the 1960s with the release of Letraset sheets containing Lorem Ipsum passages.</p>
  <div class="bar-heading" style="top:327px">1.1 Heading</div>
  <p class="body-text" style="top:368px">Lorem Ipsum is simply dummy text of the printing and typesetting industry. Lorem Ipsum has been the industry's standard dummy text ever since the 1500s, when an unknown printer took a galley of type and scrambled it to make a type specimen book. It has survived not only five centuries, but also the leap into electronic typesetting, remaining essentially unchanged. It was popularised in the 1960s with the release of Letraset sheets containing Lorem Ipsum passages.</p>
  <h3 style="left:22px;top:433px;font-family:'Varela Round',sans-serif;font-weight:400;font-size:12px">1.1.1 <span style="color:var(--red)">Heading</span></h3>
  <p class="body-text" style="left:113px;width:365px;top:435px">Lorem Ipsum is simply dummy text of the printing and typesetting industry. Lorem Ipsum has been the industry's standard dummy text ever since the 1500s, when an unknown printer took a galley of type and scrambled it to make a type specimen book.</p>
  <h4 style="left:113px;top:486px;font-weight:500;font-size:8.5px">&#10140; 1.1.1.1 <span style="color:var(--red);font-weight:400">Heading -</span></h4>
  <ul class="bullets" style="left:119px;top:506px">
    <li>Lorem Ipsum is simply dummy text of the printing and typesetting industry.</li>
    <li>Lorem Ipsum is simply dummy text of the printing and typesetting industry.</li>
    <li>Lorem Ipsum is simply dummy text of the printing and typesetting industry.</li>
    <li>Lorem Ipsum is simply dummy text of the printing and typesetting industry.</li>
    <li>Lorem Ipsum is simply dummy text of the printing and typesetting industry.</li>
  </ul>
  <div class="footer-rule"></div><div class="footer-band"></div>
  <div class="footer-url">www.bureauostrelle.net</div>
  <div class="footer-brand"><i class="dot"></i><span>Bureau<br>Ostrelle</span></div>
  <div class="footer-num">2</div>
</section>
<div class="page-label" style="left:624px;top:783px">PAGE - 02</div>

<!-- PAGE 03 -->
<section class="page" style="left:81px;top:845px">
  <h2 class="heading" style="top:48px;font-size:23px;font-weight:400"><span><b>Heading</b> Two</span></h2>
  <ul class="bullets" style="left:26px;top:97px">
    <li>Lorem Ipsum is simply dummy text of the printing and typesetting industry.</li>
    <li class="sub">Lorem Ipsum is simply dummy text of the printing and typesetting industry.</li>
    <li class="sub">Lorem Ipsum is simply dummy text of the printing and typesetting industry.</li>
    <li>Lorem Ipsum is simply dummy text of the printing and typesetting industry.</li>
    <li>Lorem Ipsum is simply dummy text of the printing and typesetting industry.</li>
    <li>Lorem Ipsum is simply dummy text of the printing and typesetting industry.</li>
    <li>Lorem Ipsum is simply dummy text of the printing and typesetting industry.</li>
    <li>Lorem Ipsum is simply dummy text of the printing and typesetting industry.</li>
  </ul>
  <h2 class="heading" style="top:271px;font-size:20px;font-weight:400"><span><b>Heading</b> Three</span></h2>
  <ul class="bullets" style="left:26px;top:318px">
    <li>Lorem Ipsum is simply dummy text of the printing and typesetting industry.</li>
    <li class="sub">Lorem Ipsum is simply dummy text of the printing and typesetting industry.</li>
    <li class="sub">Lorem Ipsum is simply dummy text of the printing and typesetting industry.</li>
    <li>Lorem Ipsum is simply dummy text of the printing and typesetting industry.</li>
    <li>Lorem Ipsum is simply dummy text of the printing and typesetting industry.</li>
    <li>Lorem Ipsum is simply dummy text of the printing and typesetting industry.</li>
    <li>Lorem Ipsum is simply dummy text of the printing and typesetting industry.</li>
    <li>Lorem Ipsum is simply dummy text of the printing and typesetting industry.</li>
    <li class="sub">Lorem Ipsum is simply dummy text of the printing and typesetting industry.</li>
    <li class="sub">Lorem Ipsum is simply dummy text of the printing and typesetting industry.</li>
  </ul>
  <div class="footer-rule"></div><div class="footer-band"></div>
  <div class="footer-url">www.bureauostrelle.net</div>
  <div class="footer-brand"><i class="dot"></i><span>Bureau<br>Ostrelle</span></div>
  <div class="footer-num">3</div>
</section>
<div class="page-label" style="left:81px;top:1569px">PAGE - 03</div>

<!-- PAGE 04 -->
<section class="page" style="left:624px;top:845px">
  <h2 class="heading" style="top:53px;font-size:16px;font-weight:400"><span><b>Heading</b> Four</span></h2>
  <p class="body-text" style="top:87px">Lorem Ipsum is simply dummy text of the printing and typesetting industry. Lorem Ipsum has been the industry's standard dummy text ever since the 1500s, when an unknown printer took a galley of type and scrambled it to make a type specimen book. It has survived not only five centuries, but also the leap into electronic typesetting, remaining essentially unchanged. It was popularised in the 1960s with the release of Letraset sheets containing Lorem Ipsum passages.</p>
  <div class="bar-heading" style="top:170px">4.1 Heading</div>
  <ul class="bullets" style="left:22px;top:215px;width:456px">
    <li style="height:33px;line-height:11px">Lorem Ipsum is simply dummy text of the printing and typesetting industry. Lorem Ipsum has been the industry's standard dummy text ever since the 1500s, when an unknown printer took a galley of type and scrambled it to make a type specimen book.</li>
    <li>Lorem Ipsum is simply dummy text of the printing and typesetting industry. Lorem Ipsum has been the industry's standard dummy.</li>
  </ul>
  <div role="img" aria-label="Photo of smiling schoolchildren crowding toward the camera" style="left:22px;top:297px;width:457px;height:141px;background:linear-gradient(90deg,#6b5a4c,#8d7462 45%,#5a4d47)"></div>
  <div class="feature" style="left:10px">
    <svg width="32" height="32" viewBox="0 0 32 32" aria-hidden="true"><g fill="none" stroke="var(--ink)" stroke-width="2"><rect x="4" y="6" width="24" height="12"/><path d="M12 6V3h8v3M16 14l-3 4 3 12 3-12z"/></g></svg>
    <h4>Title One</h4><p>Lorem Ipsum is simply dummy text of<br>the printing and typesetting industry.</p>
  </div>
  <div class="feature" style="left:174px">
    <svg width="34" height="32" viewBox="0 0 34 32" aria-hidden="true"><g fill="none" stroke="var(--ink)" stroke-width="2"><rect x="3" y="4" width="28" height="18"/><path d="M11 28h12M17 22v6M10 18V10h4v8M16 18V7h4v11M22 18v-6h3v6"/></g></svg>
    <h4>Title Two</h4><p>Lorem Ipsum is simply dummy text of<br>the printing and typesetting industry.</p>
  </div>
  <div class="feature" style="left:338px">
    <svg width="32" height="32" viewBox="0 0 32 32" aria-hidden="true"><g fill="none" stroke="var(--ink)" stroke-width="2"><path d="M6 30V3h12v27M18 12h9v18M3 30h27"/><path d="M10 8h4M10 13h4M10 18h4M10 23h4M21 17h3M21 22h3"/></g></svg>
    <h4>Title Three</h4><p>Lorem Ipsum is simply dummy text of<br>the printing and typesetting industry.</p>
  </div>
  <p class="body-text" style="top:584px">Lorem Ipsum is simply dummy text of the printing and typesetting industry. Lorem Ipsum has been the industry's standard dummy text ever since the 1500s, when an unknown printer took a galley of type and scrambled it to make a type specimen book. It has survived not only five centuries, but also the leap into electronic typesetting, remaining essentially unchanged. It was popularised in the 1960s with the release of Letraset sheets containing Lorem Ipsum passages.</p>
  <div class="footer-rule"></div><div class="footer-band"></div>
  <div class="footer-url">www.bureauostrelle.net</div>
  <div class="footer-brand"><i class="dot"></i><span>Bureau<br>Ostrelle</span></div>
  <div class="footer-num">4</div>
</section>
<div class="page-label" style="left:624px;top:1569px">PAGE - 04</div>

<!-- PAGE 05 -->
<section class="page" style="left:81px;top:1634px">
  <h2 class="heading" style="top:55px;font-size:14px;font-weight:400"><span><b>Heading</b> Five</span></h2>
  <p class="body-text" style="top:90px">Lorem Ipsum is simply dummy text of the printing and typesetting industry. Lorem Ipsum has been the industry's standard dummy text ever since the 1500s, when an unknown printer took a galley of type and scrambled it to make a type specimen book. It has survived not only five centuries, but also the leap into electronic typesetting, remaining essentially unchanged. It was popularised in the 1960s with the release of Letraset sheets containing Lorem Ipsum passages.</p>
  <table class="data-table">
    <thead><tr><th class="c1">TEXT 1</th><th class="c2">TEXT 2</th><th class="c3">TEXT 3</th><th class="c4">TEXT 4</th><th class="c5">TEXT 5</th></tr></thead>
    <tbody>
      <tr><td>Lorem Ipsum is simply text</td><td>50%</td><td>12.34</td><td>$6789</td><td>Lorem Ipsum</td></tr>
      <tr><td>Lorem Ipsum is simply text</td><td>50%</td><td>12.34</td><td>$6789</td><td>Lorem Ipsum</td></tr>
      <tr><td>Lorem Ipsum is simply text</td><td>50%</td><td>12.34</td><td>$6789</td><td>Lorem Ipsum</td></tr>
      <tr><td>Lorem Ipsum is simply text</td><td>50%</td><td>12.34</td><td>$6789</td><td>Lorem Ipsum</td></tr>
      <tr><td>Lorem Ipsum is simply text</td><td>50%</td><td>12.34</td><td>$6789</td><td>Lorem Ipsum</td></tr>
      <tr><td>Lorem Ipsum is simply text</td><td>50%</td><td>12.34</td><td>$6789</td><td>Lorem Ipsum</td></tr>
      <tr><td>Lorem Ipsum is simply text</td><td>50%</td><td>12.34</td><td>$6789</td><td>Lorem Ipsum</td></tr>
      <tr><td>Lorem Ipsum is simply text</td><td>50%</td><td>12.34</td><td>$6789</td><td>Lorem Ipsum</td></tr>
      <tr><td>Lorem Ipsum is simply text</td><td>50%</td><td>12.34</td><td>$6789</td><td>Lorem Ipsum</td></tr>
      <tr><td>Lorem Ipsum is simply text</td><td>50%</td><td>12.34</td><td>$6789</td><td>Lorem Ipsum</td></tr>
      <tr><td>Lorem Ipsum is simply text</td><td>50%</td><td>12.34</td><td>$6789</td><td>Lorem Ipsum</td></tr>
      <tr><td>Lorem Ipsum is simply text</td><td>50%</td><td>12.34</td><td>$6789</td><td>Lorem Ipsum</td></tr>
      <tr><td>Lorem Ipsum is simply text</td><td>50%</td><td>12.34</td><td>$6789</td><td>Lorem Ipsum</td></tr>
      <tr><td>Lorem Ipsum is simply text</td><td>50%</td><td>12.34</td><td>$6789</td><td>Lorem Ipsum</td></tr>
      <tr><td>Lorem Ipsum is simply text</td><td>50%</td><td>12.34</td><td>$6789</td><td>Lorem Ipsum</td></tr>
      <tr><td>Lorem Ipsum is simply text</td><td>50%</td><td>12.34</td><td>$6789</td><td>Lorem Ipsum</td></tr>
    </tbody>
  </table>
  <div class="footer-rule"></div><div class="footer-band"></div>
  <div class="footer-url">www.bureauostrelle.net</div>
  <div class="footer-brand"><i class="dot"></i><span>Bureau<br>Ostrelle</span></div>
  <div class="footer-num">5</div>
</section>
<div class="page-label" style="left:81px;top:2359px">PAGE - 05</div>

<!-- PAGE 06 : back cover -->
<section class="page" style="left:624px;top:1634px">
  <svg class="art" width="500" height="400" viewBox="0 0 500 400">
    <path d="M0,0 H500 V300 C420,305 330,300 253,280 C160,250 60,170 0,60 Z" fill="#6d7480" role="img" aria-label="Photo of two business people shaking hands in an office"/>
    <path d="M0,60 C60,170 160,250 253,280 C330,300 420,305 500,300 V343 C420,345 330,335 253,318 C150,290 50,210 0,120 Z" fill="var(--red)"/>
    <circle cx="253" cy="299" r="80" fill="#fff"/>
    <circle cx="253" cy="299" r="73" fill="var(--ink)"/>
  </svg>
  <div class="contact-text" style="top:270px;font-size:20px">Contact Us</div>
  <div class="contact-text" style="top:295px;font-size:30px;font-weight:700;font-family:'Hind',sans-serif">55-20-41</div>
  <div class="brand-dark-dot"></div>
  <div class="brand-dark">Bureau<br>Ostrelle</div>
  <svg style="left:208px;top:536px" width="84" height="22" viewBox="0 0 84 22" aria-hidden="true">
    <circle cx="11" cy="11" r="10" fill="var(--red)"/>
    <path d="M11 5a4 4 0 0 1 4 4c0 3-4 7-4 7s-4-4-4-7a4 4 0 0 1 4-4z" fill="#fff"/>
    <circle cx="42" cy="11" r="10" fill="var(--red)"/>
    <rect x="36" y="7" width="12" height="8" fill="none" stroke="#fff" stroke-width="1.4"/><path d="M36 7l6 5 6-5" fill="none" stroke="#fff" stroke-width="1.4"/>
    <circle cx="73" cy="11" r="10" fill="var(--red)"/>
    <g fill="none" stroke="#fff" stroke-width="1.2"><circle cx="73" cy="11" r="6"/><ellipse cx="73" cy="11" rx="2.6" ry="6"/><path d="M67 11h12"/></g>
  </svg>
  <div class="contact-lines">Lorem Ipsum is simply dummy text<br>hello@ostrellemail.net<br>www.ostrelle-reports.net</div>
  <div class="footer-rule"></div><div class="footer-band"></div>
</section>
<div class="page-label" style="left:624px;top:2359px">PAGE - 06</div>

</body>
</html>
```